Letterhead

We are looking for a basic letterhead. It should include our logo, website - northpeakkitchenware.com, phone 907.418.3952, toll free 855.392.6180, and fax 907.418.5263, along with our address 4837 Birchwood Lane, Anchorage, AK 99517. I want something that will look good printed in color or black and white.

```html
<!DOCTYPE html>
<html lang="en">
<head>
<meta charset="utf-8">
<title>North Peak Kitchenware Letterhead</title>
<link rel="stylesheet" href="https://fonts.googleapis.com/css2?family=Montserrat:wght@700&family=Open+Sans:wght@500&display=swap">
<style>
  :root {
    --backdrop: #857a6e;
    --paper: #ffffff;
    --brand-blue: #1f4485;
    --brand-red: #cf3a4b;
    --band-text: #ffffff;
  }
  * { margin: 0; padding: 0; box-sizing: border-box; }
  html, body {
    width: 1200px;
    height: 795px;
    overflow: hidden;
    background: var(--backdrop);
  }
  .letterhead {
    position: absolute;
    left: 314px;
    top: 27px;
    width: 572px;
    height: 740px;
    background: var(--paper);
    box-shadow: 0 6px 18px rgba(0, 0, 0, 0.25);
    overflow: hidden;
  }
  .letterhead__edge {
    position: absolute;
    left: 0;
    top: 0;
    width: 4px;
    height: 100%;
    background: var(--brand-red);
  }
  .letterhead__brand {
    position: absolute;
    left: 34px;
    top: 148px;
    font-family: "Montserrat", sans-serif;
    font-weight: 700;
    font-size: 19px;
    line-height: 1.1;
    letter-spacing: 0.02em;
    color: var(--brand-blue);
    text-transform: uppercase;
  }
  .letterhead__band {
    position: absolute;
    left: 0;
    bottom: 0;
    width: 572px;
    height: 110px;
  }
  .band__fill { fill: var(--brand-blue); }
  .band__stripe { fill: var(--brand-red); }
  .letterhead__contact {
    position: absolute;
    right: 20px;
    bottom: 12px;
    font-family: "Open Sans", sans-serif;
    font-weight: 500;
    font-size: 11.5px;
    line-height: 1.45;
    color: var(--band-text);
    text-align: right;
    font-style: normal;
  }
</style>
</head>
<body>
  <main class="letterhead">
    <div class="letterhead__edge"></div>
    <div class="letterhead__brand">North Peak<br>Kitchenware</div>

    <svg class="letterhead__band" viewBox="0 0 572 110" aria-hidden="true">
      <polygon class="band__stripe" points="0,104 572,4 572,12 0,110"/>
      <polygon class="band__fill" points="0,110 572,12 572,110"/>
    </svg>

    <address class="letterhead__contact">
      4837 Birchwood Lane, Anchorage, AK 99517<br>
      Web: northpeakkitchenware.com Phone: 907.418.3952<br>
      Tollfree: 855.392.6180 Fax: 907.418.5263
    </address>
  </main>
</body>
</html>
```